Pemberton Dialworks Business Card Design

Double Sided Business Card Design for a Locksmith company specializing in Safecracking, safe & vault service.

```html
<!DOCTYPE html>
<html lang="en">
<head>
<meta charset="utf-8">
<title>Pemberton Dialworks Business Card</title>
<link rel="stylesheet" href="https://fonts.googleapis.com/css2?family=Open+Sans:wght@300;400;700;800&display=swap">
<style>
  :root {
    --backdrop: #1a1a1a;
    --card-front: #efefef;
    --card-back: #2b2b2b;
    --brand-green: #217a3e;
    --pill-green: #4caf50;
    --text-light: #ffffff;
  }
  * { margin: 0; padding: 0; box-sizing: border-box; }
  html, body {
    width: 1200px; height: 1200px; overflow: hidden;
    background: var(--backdrop);
    font-family: "Open Sans", sans-serif;
  }
  .card {
    position: absolute; left: 216px; width: 768px; height: 439px;
  }
  .card-front { top: 135px; background: var(--card-front); }
  .card-back { top: 612px; background: var(--card-back); color: var(--text-light); }

  .brand-mark {
    position: absolute; left: 159px; top: 151px; width: 136px; height: 136px;
    border-radius: 50%; background: var(--brand-green);
  }
  .brand-name {
    position: absolute; left: 314px; top: 176px;
    color: var(--brand-green); font-weight: 800; font-size: 40px;
    line-height: 46px; letter-spacing: 1px; text-transform: uppercase;
  }

  .centered { position: absolute; left: 0; width: 100%; text-align: center; }
  .company-line { top: 111px; font-weight: 300; font-size: 21px; }
  .name-pill {
    position: absolute; left: 184px; top: 143px; width: 400px; height: 71px;
    border-radius: 36px; background: var(--pill-green);
    display: flex; align-items: center; justify-content: center;
    font-weight: 700; font-size: 50px; letter-spacing: 0.5px;
  }
  .address-line { top: 227px; font-weight: 300; font-size: 20px; }
  .divider {
    position: absolute; left: 354px; top: 261px; width: 73px; height: 1px;
    background: var(--pill-green);
  }
  .contact-line { top: 270px; font-weight: 300; font-size: 20px; }
  .contact-line b { font-weight: 700; }
  .web-line { top: 296px; font-weight: 700; font-size: 19px; }
</style>
</head>
<body>
  <section class="card card-front">
    <div class="brand-mark"></div>
    <div class="brand-name">Pemberton<br>Dialworks</div>
  </section>

  <section class="card card-back">
    <p class="centered company-line">Pemberton Dialworks LLC</p>
    <div class="name-pill">Elena Marsh</div>
    <p class="centered address-line">1480 Harwick Lane, Suite 210 Brookfield , TX , 75340</p>
    <div class="divider"></div>
    <p class="centered contact-line"><b>t:</b> 555-014-2270 &nbsp;|&nbsp; <b>e:</b> office@dialworks.com</p>
    <p class="centered web-line">www.pembertondialworks.com</p>
  </section>
</body>
</html>
```